Business card for apparel company. Specializing in fishing and boating performance wear. Main company name is Marlowe Teal Company, LLC brand name for apparel is WAKEFIN. See website www.WakefinReefline.com I will attach some logos to consider.

```html
<!DOCTYPE html>
<html lang="en">
<head>
<meta charset="utf-8">
<title>Marlowe Teal Company, LLC — WAKEFIN business card</title>
<link href="https://fonts.googleapis.com/css2?family=Poppins:wght@400;700;800&display=swap" rel="stylesheet">
<style>
  :root{
    --stage:#3b3b3b;
    --blue-light:#06a9e6;
    --blue-deep:#0466d6;
    --blue-brand:#0a7fe0;
    --blue-emboss:#0b5fae;
    --ink:#1c1c1c;
    --paper:#ffffff;
    --rule:#9a9a9a;
  }
  *{box-sizing:border-box;margin:0;padding:0}
  html,body{width:1200px;height:689px;overflow:hidden;background:var(--stage)}
  body{font-family:"Poppins",sans-serif;position:relative}
  .card{position:absolute;top:196px;width:520px;height:297px;border-radius:22px;overflow:hidden}
  .card-front{left:50px;background:linear-gradient(160deg,var(--blue-light),var(--blue-deep))}
  .card-back{left:630px;background:var(--paper)}
  .front-name{position:absolute;inset:0;display:flex;align-items:center;justify-content:center;
    font-weight:800;font-size:64px;letter-spacing:4px;color:var(--blue-emboss)}
  .back-brand{position:absolute;left:28px;top:92px;width:210px;display:flex;align-items:center;gap:10px}
  .back-brand .mark{width:22px;height:22px;border-radius:50%;background:var(--blue-brand);flex:none}
  .back-brand .name{font-weight:800;font-size:36px;color:var(--blue-brand);letter-spacing:1px;white-space:nowrap}
  .divider{position:absolute;left:252px;top:34px;width:1px;height:170px;background:var(--rule)}
  .contact{position:absolute;left:272px;top:32px;color:var(--ink);font-size:12.5px;line-height:1.45}
  .contact .person{font-weight:700;font-size:16px;color:var(--blue-brand);letter-spacing:.5px;line-height:1.1}
  .contact .role{font-size:12.5px;margin-bottom:8px}
  .contact .row{display:flex;align-items:center;gap:7px;white-space:nowrap}
  .contact .row svg{width:11px;height:11px;flex:none}
  .contact .web-accent{color:var(--blue-brand)}
  .contact .address{margin-top:8px}
  .bands{position:absolute;left:0;bottom:0;width:100%;height:60px}
</style>
</head>
<body>
  <section class="card card-front" aria-label="Card front">
    <div class="front-name">WAKEFIN</div>
  </section>

  <section class="card card-back" aria-label="Card back">
    <div class="back-brand"><span class="mark"></span><span class="name">WAKEFIN</span></div>
    <div class="divider"></div>
    <div class="contact">
      <div class="person">CALDER VOSS</div>
      <div class="role">Managing Director</div>
      <div class="row">
        <svg viewBox="0 0 12 12"><path d="M3 1l2 2.5-1.2 1.2a7 7 0 0 0 3.5 3.5L8.5 7 11 9l-1.5 2C5 11 1 7 1 2.5z" fill="var(--blue-brand)"/></svg>
        <span>044-555 210 347</span></div>
      <div class="row">
        <svg viewBox="0 0 12 12"><rect x="1" y="2.5" width="10" height="7" fill="var(--blue-brand)"/><path d="M1 2.5l5 4 5-4" stroke="#fff" stroke-width="1" fill="none"/></svg>
        <span>info@wakefinreefline.com</span></div>
      <div class="row">
        <svg viewBox="0 0 12 12"><circle cx="6" cy="6" r="5" fill="var(--blue-brand)"/><path d="M1 6h10M6 1c-2.5 3-2.5 7 0 10M6 1c2.5 3 2.5 7 0 10" stroke="#fff" stroke-width=".7" fill="none"/></svg>
        <span>www.<span class="web-accent">WakefinReefline</span>.com</span></div>
      <div class="address">88, Harbor Pier Road<br>70913, Gulf Shores</div>
    </div>
    <svg class="bands" viewBox="0 0 520 60" preserveAspectRatio="none" aria-hidden="true">
      <rect x="0" y="28" width="520" height="4" fill="var(--blue-brand)"/>
      <rect x="0" y="38" width="520" height="22" fill="var(--blue-brand)"/>
      <circle cx="470" cy="30" r="26" fill="var(--paper)"/>
      <circle cx="470" cy="30" r="20" fill="var(--blue-brand)"/>
    </svg>
  </section>
</body>
</html>
```